Ledgerwise Reach - B2B Demand Generation Website Project

We need a fully functional website for www.ledgerwisereach.example. We are a B2B Demand Generation company, based in London, working with companies such as QRT, VKD, Norvex, Brindlow, Tarvo generating them sales leads for their sales teams. We run this through digital marketing newsletter promotions and have a network of websites. Content syndication, data, demand generation, online marketing. Our logo has just been redone (attached) and we have a holding page already which i would like to use the style / colours. Our logo is bright and vibrant but i dont want the site to be a rainbow. We are expensive, classy, professorial, B2B, intelligent.

Home
About Us
Our Services
Prospora & QA Technology
Intent Data
Testimonials
Contact Us
Updates

Target Market(s)

B2B Marketers (QRT, Velquarion, Tarvo, VKD, Opal Reach, Driftmoor, Harlow Quantis, Technology Companies, Data Companies, Marketing Teams, Tumbleden.

Industry/Entity Type

Marketing

Coding

Coded - Design and coding required

Number of Pages Required

5+ page

Font styles to use
Sans Serif

Requirements
Must have
• Home
About Us
Our Services
Prospora & QA Technology
Intent Data
Testimonials
Contact Us

Simple Pages.

Look classy, intelligent, data experts. I like the video homepages were the image moves at the top. Very soft animation.
Nice to have
• Websites i like:

https://www.vkd.example/
https://www.brevantor.example/
https://www.plumfieldsites.example.co.uk/

Ledgerwise Reach - The Demand Generation Company
Should not have
• Glimpsevault crap images

```html
<!DOCTYPE html>
<html lang="en">
<head>
<meta charset="utf-8">
<title>Ledgerwise Reach - The Demand Generation Company</title>
<link rel="stylesheet" href="https://fonts.googleapis.com/css2?family=Montserrat:wght@300;400;800&family=Karla:wght@400&family=Oswald:wght@400;500&display=swap">
<style>
  :root {
    --page-bg: #ffffff;
    --navy: #020a14;
    --deep-blue: #0b3550;
    --teal: #2f7fa6;
    --white: #ffffff;
    --band-red: #4a1010;
    --brand-red: #c4262e;
    --brand-blue: #2a6fb0;
    --menu-grey: #9b9fa3;
    --muted-grey: #7d8185;
  }
  * { box-sizing: border-box; margin: 0; padding: 0; }
  html, body { width: 1008px; height: 1200px; overflow: hidden; background: var(--page-bg); }
  body { position: relative; font-family: "Karla", sans-serif; }

  .screen {
    position: absolute;
    left: 54px;
    width: 900px;
    height: 561px;
    overflow: hidden;
    color: var(--white);
  }
  .screen--home { top: 26px; }
  .screen--menu { top: 613px; }

  .hero-visual {
    position: absolute; inset: 0;
    background:
      radial-gradient(circle at 24% 50%, #000 0 7%, rgba(0,0,0,0) 18%),
      radial-gradient(ellipse at 30% 45%, var(--deep-blue) 0%, rgba(11,53,80,0.6) 30%, rgba(2,10,20,0) 60%),
      radial-gradient(ellipse at 75% 55%, var(--teal) 0%, #164e6d 30%, var(--navy) 75%),
      var(--navy);
  }
  .menu-visual {
    position: absolute; inset: 0;
    background:
      radial-gradient(ellipse at 30% 50%, #0a1a26 0%, rgba(0,0,0,0) 50%),
      radial-gradient(ellipse at 75% 55%, #1d2a33 0%, #0c1217 40%, #020304 80%),
      #020304;
  }

  .brand {
    position: absolute; left: 30px; top: 22px;
    display: flex; flex-direction: column; align-items: center;
    width: 182px;
  }
  .brand__dot { width: 40px; height: 40px; border-radius: 50%; background: var(--brand-red); }
  .brand__name {
    margin-top: 12px;
    font-family: "Montserrat", sans-serif; font-weight: 400;
    font-size: 19px; letter-spacing: -0.3px;
    color: var(--brand-red);
  }

  .tools { position: absolute; left: 796px; top: 30px; display: flex; gap: 16px; align-items: center; }

  .hero-copy { position: absolute; left: 451px; top: 152px; width: 360px; }
  .hero-copy__title {
    font-family: "Montserrat", sans-serif; font-weight: 300;
    font-size: 24px; line-height: 26px; letter-spacing: 0.2px;
  }
  .hero-copy__title strong { font-weight: 800; }
  .hero-copy__text { margin-top: 22px; font-size: 12px; line-height: 16.6px; }
  .hero-copy__button {
    display: inline-block; margin-top: 20px;
    width: 164px; height: 36px; line-height: 34px;
    border: 1px solid var(--white); text-align: center;
    font-family: "Montserrat", sans-serif; font-weight: 800; font-size: 14px; letter-spacing: 0.5px;
  }
  .scroll-cue { position: absolute; left: 859px; top: 274px; }

  .stats-band {
    position: absolute; left: 0; top: 476px; width: 900px; height: 85px;
    background: var(--band-red);
  }
  .stat { position: absolute; top: 17px; display: flex; align-items: center; gap: 12px; }
  .stat--downloads { left: 84px; }
  .stat--leads { left: 345px; }
  .stat--reach { left: 609px; }
  .stat__value { font-family: "Montserrat", sans-serif; font-weight: 300; font-size: 30px; line-height: 30px; }
  .stat__label { font-family: "Montserrat", sans-serif; font-weight: 400; font-size: 9.5px; letter-spacing: 0.6px; margin-top: 3px; }

  .close { position: absolute; left: 796px; top: 29px; display: flex; align-items: center; gap: 8px; }
  .close__label { font-family: "Oswald", sans-serif; font-weight: 400; font-size: 14px; letter-spacing: 0.4px; color: #c9cccf; }

  .main-nav { position: absolute; right: 32px; top: 105px; text-align: right; list-style: none; }
  .main-nav li {
    font-family: "Montserrat", sans-serif; font-weight: 800; font-size: 25px;
    line-height: 42px; color: var(--menu-grey);
  }
  .main-nav .is-current { color: #3a3c3f; text-decoration: line-through; text-decoration-color: var(--brand-red); text-decoration-thickness: 4px; }

  .contact { position: absolute; right: 32px; top: 440px; text-align: right; font-family: "Oswald", sans-serif; }
  .contact__line { font-weight: 500; font-size: 13px; line-height: 17px; color: #e3e5e7; }
  .contact__legal { margin-top: 24px; font-size: 9.5px; color: var(--muted-grey); letter-spacing: 0.4px; }
  .socials { display: flex; justify-content: flex-end; gap: 15px; margin-top: 18px; }
  .socials span { width: 9px; height: 9px; border-radius: 50%; background: var(--muted-grey); }
</style>
</head>
<body>

<section class="screen screen--home">
  <div class="hero-visual" role="img" aria-label="Deep blue swirl of glowing dots curving into a dark centre"></div>

  <div class="brand">
    <span class="brand__dot"></span>
    <span class="brand__name">ledgerwisereach</span>
  </div>

  <div class="tools">
    <svg width="26" height="26" viewBox="0 0 26 26" fill="none" stroke="#fff" stroke-width="2.2">
      <circle cx="11" cy="11" r="9"/><line x1="17.5" y1="17.5" x2="24" y2="24"/>
    </svg>
    <svg width="30" height="26" viewBox="0 0 30 26" fill="#fff">
      <rect x="0" y="0" width="30" height="2.6"/><rect x="10" y="7.8" width="20" height="2.6"/>
      <rect x="4" y="15.6" width="26" height="2.6"/><rect x="0" y="23.4" width="30" height="2.6"/>
    </svg>
  </div>

  <div class="hero-copy">
    <h1 class="hero-copy__title">DELIVERING YOUR <strong>DEMAND GENERATION STRATEGY</strong></h1>
    <p class="hero-copy__text">Ledgerwise Reach offers multi-channel demand generation services to publishers and technology vendors through our network of lead generation websites and native speaking telemarketing agents. Whether looking for MQL, ABM or BANT campaigns, Ledgerwise Reach can assist you in delivering your demand generation strategy and generate pipeline for your sales teams and/or channel partners.</p>
    <span class="hero-copy__button">GET STARTED</span>
  </div>

  <svg class="scroll-cue" width="12" height="26" viewBox="0 0 12 26" fill="none" stroke="#fff" stroke-width="1.8">
    <rect x="2" y="1" width="8" height="7"/><line x1="6" y1="11" x2="6" y2="23"/>
    <polyline points="2,19 6,24 10,19" fill="#fff"/>
  </svg>

  <div class="stats-band">
    <div class="stat stat--downloads">
      <svg width="44" height="48" viewBox="0 0 44 48" fill="none" stroke="#fff" stroke-width="4">
        <path d="M12 14H4v31h36V14h-8"/><line x1="22" y1="2" x2="22" y2="30"/><polyline points="12,21 22,31 32,21"/>
      </svg>
      <div><div class="stat__value">70,000+</div><div class="stat__label">DOWNLOADS PER MONTH</div></div>
    </div>
    <div class="stat stat--leads">
      <svg width="48" height="44" viewBox="0 0 48 44" fill="#fff">
        <path d="M2 16h8l20-10v30L10 26H2z"/><rect x="9" y="27" width="6" height="12" rx="2"/>
        <circle cx="41" cy="6" r="2.5"/><circle cx="41" cy="16" r="2.5"/><circle cx="41" cy="26" r="2.5"/><circle cx="41" cy="36" r="2.5"/>
      </svg>
      <div><div class="stat__value">25,000+</div><div class="stat__label">LEADS DELIVERED PER MONTH</div></div>
    </div>
    <div class="stat stat--reach">
      <svg width="48" height="48" viewBox="0 0 48 48" fill="none" stroke="#fff" stroke-width="2.5">
        <circle cx="24" cy="24" r="21"/><ellipse cx="24" cy="24" rx="9" ry="21"/><line x1="3" y1="24" x2="45" y2="24"/>
      </svg>
      <div><div class="stat__value">50+</div><div class="stat__label">COUNTRIES WE CAN REACH</div></div>
    </div>
  </div>
</section>

<section class="screen screen--menu">
  <div class="menu-visual" role="img" aria-label="Dimmed dark version of the dotted swirl background"></div>

  <div class="brand">
    <span class="brand__dot"></span>
    <span class="brand__name">ledgerwisereach</span>
  </div>

  <div class="close">
    <span class="close__label">CLOSE</span>
    <svg width="32" height="32" viewBox="0 0 32 32" stroke="#fff" stroke-width="1.5">
      <line x1="1" y1="1" x2="31" y2="31"/><line x1="31" y1="1" x2="1" y2="31"/>
    </svg>
  </div>

  <ul class="main-nav">
    <li class="is-current">HOME</li>
    <li>ABOUT US</li>
    <li>OUR SERVICES</li>
    <li>PROSPORA &amp; QA TECHNOLOGY</li>
    <li>INTENT DATA</li>
    <li>TESTIMONIALS</li>
    <li>CONTACT</li>
  </ul>

  <div class="contact">
    <p class="contact__line">HELLO@LEDGERWISEREACH.EXAMPLE</p>
    <p class="contact__line">TEL: +442079460321</p>
    <p class="contact__legal">PRIVACY POLICY - TERMS OF USE</p>
    <div class="socials"><span></span><span></span><span></span><span></span><span></span></div>
  </div>
</section>

</body>
</html>
```